Dermacare Nurse Alliance - Rack Card Design

This is a 2-sided rack card that should be 3.5 inches wide by 8.5 inches tall.

Text (with instructions), logo and website image are attached. For the main image on the front, you can use the attached image, or pull whatever you like off of stockpixelvault.example, and we will purchase the photo from the winning design

The front should have text plus a nurse image, the back should have mostly text with the website image and legend.
Updates

We have received many high quality designs, but it is apparent to us that at the print size we are currently using (3.5x8.5), that the image of the homepage on the back is too small, and not legible. As such, we have decided that we would like to go with a horizontal version at 8.5 wide by 5.5 tall, with a larger more legible version of the website on the back and call outs to one side or the other, please resubmit your designs in that format. Thank you, and sorry for the inconvenience. Ned

Industry/Entity Type

Nurse

Font styles to use
Sans Serif

Colors
876aae
6b449b
b7a5cd
e4daeb

Requirements
Must have
• Please use the color palate from the attached logo, and a nursing image on the front.

```html
<!DOCTYPE html>
<html lang="en">
<head>
<meta charset="utf-8">
<title>Dermacare Nurse Alliance – Rack Card</title>
<link rel="stylesheet" href="https://fonts.googleapis.com/css2?family=Quicksand:wght@400;500;700&display=swap">
<style>
  :root {
    --purple-mid: #876aae;
    --purple-deep: #6b449b;
    --purple-soft: #b7a5cd;
    --purple-pale: #e4daeb;
    --purple-tri: #a390c7;
    --purple-tri-light: #cbbfe0;
    --grey-text: #9a9a9a;
    --white: #ffffff;
  }
  * { margin: 0; padding: 0; box-sizing: border-box; }
  html, body { width: 1200px; height: 777px; overflow: hidden; background: var(--white); }
  .card {
    position: relative;
    width: 1200px;
    height: 777px;
    font-family: "Quicksand", sans-serif;
    background: var(--white);
    overflow: hidden;
  }
  .shapes { position: absolute; inset: 0; }
  .tagline { position: absolute; color: var(--purple-deep); }
  .tagline .lead { display: block; font-weight: 400; font-size: 58px; line-height: 1; color: var(--purple-deep); }
  .tagline .sub { display: block; font-weight: 700; font-size: 31px; line-height: 1; color: var(--grey-text); }
  .tagline-inspired { left: 40px; top: 44px; text-align: right; width: 210px; }
  .tagline-inspired .sub { margin-top: 8px; }
  .tagline-empowered { left: 314px; top: 174px; }
  .tagline-empowered .sub { margin-top: 12px; margin-left: -2px; }
  .rule { position: absolute; width: 5px; background: var(--purple-soft); }
  .rule-inspired { left: 262px; top: 46px; height: 91px; }
  .rule-empowered { left: 296px; top: 175px; height: 91px; }
  .band-title {
    position: absolute;
    right: 25px;
    top: 182px;
    color: var(--white);
    font-size: 34px;
    font-weight: 400;
    letter-spacing: 0.3px;
  }
  .band-title strong { font-weight: 700; }
  .brand {
    position: absolute;
    left: 32px;
    top: 598px;
    display: flex;
    align-items: center;
    height: 120px;
  }
  .brand-foundation {
    width: 160px;
    display: flex;
    align-items: center;
    gap: 8px;
    font-weight: 700;
    font-size: 21px;
    line-height: 1.15;
    color: var(--purple-deep);
  }
  .brand-dot { width: 16px; height: 16px; border-radius: 50%; background: var(--purple-deep); flex: none; }
  .brand-divider { width: 2px; height: 120px; background: var(--purple-deep); margin: 0 14px 0 8px; }
  .brand-alliance {
    font-weight: 700;
    font-size: 30px;
    line-height: 1.1;
    color: var(--purple-deep);
  }
  .web-link {
    position: absolute;
    left: 32px;
    top: 737px;
    width: 332px;
    height: 40px;
    background: var(--purple-mid);
    color: var(--white);
    font-size: 19px;
    font-weight: 500;
    display: flex;
    align-items: center;
    justify-content: center;
  }
</style>
</head>
<body>
<main class="card">
  <svg class="shapes" width="1200" height="777" viewBox="0 0 1200 777">
    <defs>
      <linearGradient id="team-photo-tone" gradientUnits="userSpaceOnUse" x1="0" y1="235" x2="0" y2="777">
        <stop offset="0" stop-color="#c4876a"/>
        <stop offset="0.18" stop-color="#dca47c"/>
        <stop offset="0.34" stop-color="#e7bf95"/>
        <stop offset="0.46" stop-color="#a98a8c"/>
        <stop offset="0.56" stop-color="#44568f"/>
        <stop offset="0.75" stop-color="#2f4380"/>
        <stop offset="1" stop-color="#24346b"/>
      </linearGradient>
      <linearGradient id="scrubs-photo-tone" x1="0" y1="0" x2="1" y2="1">
        <stop offset="0" stop-color="#8b9cc4"/>
        <stop offset="0.6" stop-color="#aeb8d6"/>
        <stop offset="1" stop-color="#dfe1ee"/>
      </linearGradient>
    </defs>
    <polygon class="photo-side" role="img" aria-label="Close-up of a nurse in scrubs with a stethoscope, holding books"
      points="0,151 314,334 0,515" fill="url(#scrubs-photo-tone)"/>
    <polygon class="photo-main" role="img" aria-label="Four smiling nurses in navy scrubs standing with arms crossed outside a hospital entrance"
      points="390,376 672,235 1200,235 1200,777 390,777" fill="url(#team-photo-tone)"/>
    <polygon class="title-band" points="748,173 1200,173 1200,235 644,235" fill="var(--purple-deep)"/>
    <polygon points="757,4 799,28 757,52" fill="var(--purple-deep)"/>
    <polygon points="801,32 801,133 712,80" fill="var(--purple-tri-light)"/>
    <polygon points="805,32 877,74 805,117" fill="var(--purple-pale)"/>
    <polygon points="686,72 797,137 686,201" fill="var(--purple-tri)"/>
    <polygon points="272,361 385,425 272,489" fill="var(--purple-tri)"/>
    <polygon points="299,483 385,433 385,531" fill="var(--purple-tri-light)"/>
    <polygon points="345,511 385,531 345,555" fill="var(--purple-deep)"/>
  </svg>

  <span class="rule rule-inspired"></span>
  <h2 class="tagline tagline-inspired">
    <span class="lead">Inspired</span>
    <span class="sub">by patients</span>
  </h2>

  <span class="rule rule-empowered"></span>
  <h2 class="tagline tagline-empowered">
    <span class="lead">Empowered</span>
    <span class="sub">by knowledge</span>
  </h2>

  <h1 class="band-title">Impacting <strong>MELANOMA</strong></h1>

  <div class="brand">
    <div class="brand-foundation"><span class="brand-dot"></span><span>Crestline Skin Foundation</span></div>
    <span class="brand-divider"></span>
    <div class="brand-alliance">Dermacare<br>Nurse<br>Alliance</div>
  </div>

  <div class="web-link">www.DermacareNurse.example</div>
</main>
</body>
</html>
```